Web Design for Webdesign company 3 page PSD

Project
---------
We need a PSD Web Design to be used in a WordPress installation.
What we would like to create is a professional looking website for a web design agency. We also need you to look for suitable stock images to be placed on these pages.
We need the design for:
Homepage
Landing page
Contact page
attached in the pages file you will find a file with more in depth details how these files should be build up.
We would like to see a desktop version and a mobile version of these pages
The website should have a 1100px width.
The mobile design should have 480px width.
The homepage should have a header slider about 450px high.
The slider is preferred full width and should have some images text and a button
Objectives
-------------
The main objective for the website is to get leads from customers in the form of a request for a quotation or a call or mail me back action. The most important action for the homepage is to link and navigate to our landing pages.
What we want to tell our visitors (our main products)
-------------------------------------------------------------------
- A website with no big investment but a monthly rate
- A successful website with no worries (a complete website, seo, hosting and a service contract for future customization is included for a monthly rate)
Color Scheme
------------
Use branding colors. You can find them in the branding.pdf file.
Additional colors:
White: #ffffff
Black: #181818
Company info
--------------
We are a starting web design / marketing agency based in The Netherlands and looking for the design of our website. Our services are (custom) webdesign, website marketing or combinations of both. Our main customer group is small business owners.
We sell websites but give the option to buy it with a lease contract.
A second product is a default website with a complete service: SEO, hosting and a service contract for a monthly rate.
Content:
-----------
If not available place Lorem Ipsum text.
There will come about 400 words of text on the landing pages
Design Competition
--------------------------
Since this is a designing competition we would like to see your creativity.
What you can expect from us is a lot of feedback 7 days a week with short response time.
You can send us the first sketchy mock ups of the homepage and we will give feedback based on these design. But we like your feedback or comments as well
Read the pages file for more in depth details how the pages should be designed

Target Market(s)
Small business owners in The Netherlands
Industry/Entity Type
It Company
Number of Pages Required
3 page
Requirements
Must have
- Homepage:
- Header slider with images, some text and a link to a custom page
- The slider should have 3 designed slides
- Landings page:
- Sidebar
- Action button for a request for a quotation
- Action button for a call me back action
- Action button for an appointment
- Contact form:
- Address details
- Contact form
Nice to have
- Homepage:
- Full width slider
- Testimonial block
- Blog items
Should not have
- Flash
- A to crowded design

```html
<!DOCTYPE html>
<html lang="en">
<head>
<meta charset="utf-8">
<title>Vellamoor — Web Design</title>
<link href="https://fonts.googleapis.com/css2?family=Open+Sans:wght@300;400;600&family=Oswald:wght@300;400&display=swap" rel="stylesheet">
<style>
:root{
  --green:#4b8a5e;
  --green-dark:#3c7550;
  --ink:#181818;
  --text:#555;
  --muted:#888;
  --dark:#2f2f2f;
  --dark-2:#3b3b3b;
  --band:#6d6d6d;
  --line:#dcdcdc;
  --white:#ffffff;
}
*{box-sizing:border-box;margin:0;padding:0}
html,body{width:698px;height:1200px;overflow:hidden}
body{font-family:"Open Sans",Arial,sans-serif;color:var(--text);background:var(--white);font-size:11px}
.page{position:relative;width:698px;height:1200px}

/* hero */
.hero{position:absolute;top:0;left:0;width:698px;height:445px;background:radial-gradient(ellipse at 60% 45%,#4a4a4a 0%,#333 55%,#262626 100%)}
.brand{position:absolute;left:26px;top:14px;display:flex;align-items:center;gap:8px}
.brand-mark{width:26px;height:26px;border-radius:50%;background:var(--green)}
.brand-name{font-family:"Oswald",sans-serif;font-size:17px;color:var(--green);letter-spacing:1px;line-height:1}
.brand-tag{font-size:7px;color:#bbb;margin-top:3px}
.nav{position:absolute;right:30px;top:30px;display:flex;gap:22px}
.nav a{color:var(--white);font-size:10px;text-decoration:none}
.hero-copy{position:absolute;left:30px;top:82px;width:340px}
.hero-title{font-weight:300;color:#e8e8e8;font-size:45px;line-height:50px}
.hero-title span{display:block}
.hero-sub{font-weight:300;color:#ddd;font-size:18px;line-height:24px;margin-top:10px}
.hero-sub b{color:var(--green);font-weight:400}
.btn{display:inline-block;font-size:10px;padding:7px 16px;text-decoration:none}
.btn-solid{background:var(--green);color:var(--white);margin:22px 0 0 140px}
.hero-visual{position:absolute;left:368px;top:70px;width:300px;height:290px;border-radius:6px;background:linear-gradient(135deg,#5b5b5b,#3c3c3c)}
.dots{position:absolute;top:418px;left:0;width:100%;display:flex;justify-content:center;gap:6px}
.dots i{width:11px;height:11px;border-radius:50%;border:2px solid #bbb;background:#666}

/* welcome */
.welcome{position:absolute;top:465px;left:0;width:698px;height:210px}
.welcome-visual{position:absolute;left:40px;top:10px;width:205px;height:180px;border-radius:4px;background:linear-gradient(160deg,#e7ecef,#c9d3d9)}
.welcome-body{position:absolute;left:290px;top:20px;width:360px}
.section-title{display:flex;align-items:center;gap:10px;font-family:"Oswald",sans-serif;font-weight:300;font-size:22px;color:#444}
.section-title .accent{color:var(--green)}
.leaf-badge{width:26px;height:26px;border-radius:50%;background:var(--green);display:flex;align-items:center;justify-content:center}
.welcome-text{margin:12px 0 0 36px;font-size:9.5px;line-height:14px;color:var(--muted)}
.btn-outline{border:1px solid var(--green);color:var(--green);margin:16px 0 0 150px}

/* services band */
.band{position:absolute;top:683px;left:0;width:698px;height:74px;background:var(--band)}
.band-tab{position:absolute;left:50%;transform:translateX(-50%);top:27px;background:var(--white);display:flex;align-items:center;gap:8px;padding:5px 14px;font-family:"Oswald",sans-serif;font-weight:300;font-size:13px;color:#333}
.band-tab i{width:14px;height:14px;border-radius:50%;background:var(--green)}

/* testimonials */
.customers{position:absolute;top:775px;left:0;width:698px}
.customers .section-title{justify-content:center}
.cards{display:flex;justify-content:center;gap:25px;margin-top:20px}
.card{width:170px;height:140px;border:1px solid var(--line);padding:16px 18px;position:relative}
.card p{font-size:9px;line-height:13px;color:var(--muted)}
.card-author{position:absolute;left:18px;bottom:14px;display:flex;align-items:center;gap:10px;font-size:9px;color:var(--muted)}
.avatar{width:30px;height:30px;border-radius:50%;background:#b9b9b9}

/* footer */
.contact-bar{position:absolute;top:985px;left:0;width:698px;height:76px;background:var(--dark-2);color:#ddd}
.contact-block{position:absolute;top:18px;display:flex;gap:10px;align-items:flex-start}
.icon-circle{width:30px;height:30px;border-radius:50%;background:#555;display:flex;align-items:center;justify-content:center}
.contact-block h4{font-size:11px;font-weight:600;color:var(--white);margin-bottom:3px}
.contact-block p{font-size:9px;line-height:13px;color:#ccc}
.search{position:absolute;right:40px;top:22px;width:150px;height:24px;border:1px solid #888;display:flex;align-items:center;justify-content:space-between;padding:0 8px;font-size:9px;color:#bbb}
.map{position:absolute;top:1061px;left:0;width:698px;height:118px;background:linear-gradient(135deg,#dfe6d6,#c9d8e4)}
.legal{position:absolute;top:1179px;left:0;width:698px;height:21px;background:var(--dark);color:#bbb;font-size:8px;text-align:center;line-height:21px}
.legal b{color:var(--green);font-weight:400}
</style>
</head>
<body>
<div class="page">

  <header class="hero">
    <div class="brand">
      <div class="brand-mark"></div>
      <div>
        <div class="brand-name">VELLAMOOR</div>
        <div class="brand-tag">Your own website, built right</div>
      </div>
    </div>
    <nav class="nav">
      <a href="#">Home</a><a href="#">About</a><a href="#">Web design</a><a href="#">Services</a><a href="#">Contact</a>
    </nav>
    <div class="hero-copy">
      <h1 class="hero-title"><span>Successful</span><span>websites with</span><span>total care</span></h1>
      <p class="hero-sub">Optimized website with <b>maintenance</b> and <b>hosting</b></p>
      <a class="btn btn-solid" href="#">Read More</a>
    </div>
    <div class="hero-visual" role="img" aria-label="Laptop showing code surrounded by web technology icons"></div>
    <div class="dots"><i></i><i></i><i></i></div>
  </header>

  <section class="welcome">
    <div class="welcome-visual" role="img" aria-label="Hand holding a laptop displaying a website"></div>
    <div class="welcome-body">
      <h2 class="section-title"><span class="leaf-badge"></span><span>Welcome to <span class="accent">VELLAMOOR</span></span></h2>
      <p class="welcome-text">Lorem Ipsum is simply dummy text of the printing and typesetting industry. Lorem Ipsum has been the industry's standard dummy text ever since the 1500s, when an unknown printer took a galley of type and scrambled it to make a type specimen book. It has survived not only five centuries, but also the leap.</p>
      <a class="btn btn-outline" href="#">Read More</a>
    </div>
  </section>

  <section class="band" role="img" aria-label="Grey band with faint leaf pattern">
    <div class="band-tab"><i></i>Web Design</div>
  </section>

  <section class="customers">
    <h2 class="section-title"><span class="leaf-badge"></span>Our Happy Customer</h2>
    <div class="cards">
      <article class="card">
        <p>Lorem Ipsum is simply dummy text of the printing and typesetting industry. Lorem Ipsum has been the industry's standard dummy text.</p>
        <div class="card-author"><span class="avatar" role="img" aria-label="Customer portrait"></span>JOHN DOE</div>
      </article>
      <article class="card">
        <p>Lorem Ipsum is simply dummy text of the printing and typesetting industry. Lorem Ipsum has been the industry's standard dummy text.</p>
        <div class="card-author"><span class="avatar" role="img" aria-label="Customer portrait"></span>JOHN DOE</div>
      </article>
      <article class="card">
        <p>Lorem Ipsum is simply dummy text of the printing and typesetting industry. Lorem Ipsum has been the industry's standard dummy text.</p>
        <div class="card-author"><span class="avatar" role="img" aria-label="Customer portrait"></span>JOHN DOE</div>
      </article>
    </div>
  </section>

  <footer>
    <div class="contact-bar">
      <div class="contact-block" style="left:60px">
        <span class="icon-circle"><svg width="14" height="14" viewBox="0 0 14 14"><path d="M1 7 7 1.5 13 7M3 6v6h3V9h2v3h3V6" fill="none" stroke="#fff" stroke-width="1.5"/></svg></span>
        <div>
          <h4>Vellamoor Web Services</h4>
          <p>20 A, Office area name,<br>City, State, Country</p>
        </div>
      </div>
      <div class="contact-block" style="left:270px">
        <span class="icon-circle"><svg width="14" height="14" viewBox="0 0 14 14"><path d="M3 1.5h2.5l1 3-1.5 1a7 7 0 0 0 3.5 3.5l1-1.5 3 1V11a1.5 1.5 0 0 1-1.5 1.5A10 10 0 0 1 1.5 3 1.5 1.5 0 0 1 3 1.5z" fill="#fff"/></svg></span>
        <div>
          <p>Phone no. : +31 20 555 0142</p>
          <p>Email : info@vellamoor.example</p>
        </div>
      </div>
      <div class="search">Search....<svg width="10" height="10" viewBox="0 0 10 10"><circle cx="4" cy="4" r="3" fill="none" stroke="#bbb" stroke-width="1.3"/><path d="M6.3 6.3 9.3 9.3" stroke="#bbb" stroke-width="1.3"/></svg></div>
    </div>
    <div class="map" role="img" aria-label="Street map of the office location"></div>
    <div class="legal">© 2015 <b>Vellamoor</b>. All Rights Reserved.</div>
  </footer>

</div>
</body>
</html>
```